Professional DJ Business Card

Business card for giving out to clubs and venues or interested groups that are in need of a professional DJ. I want something artistic and catchy/alluring, with a minimalist approach that gets just the vital amount of info and leaves the rest for inquiry via contacting me. Ideally I would like one side to have an image of something cool like an eye and my name, then the other side be the contact info, I am definitely feeling a black or dark colored card, but I am open to other designs. I am uploading a picture that I made that reflects a little of what I am *kind of* looking for.

Industry/Entity Type

Business

Contact Information for Business Card

Tomas Halvik (Voxtel)
Professional DJ (West Coast)
EDM (Deep/House/Techno), Hip Hop, Latin, Trap.
Cell: 555-274-9163
Email: Voxtelofficial@mailnest.net
www.beatcloudia.net/yourtuneisfading

```html
<!DOCTYPE html>
<html lang="en">
<head>
<meta charset="utf-8">
<title>Voxtel – Professional DJ Business Card</title>
<link rel="stylesheet" href="https://fonts.googleapis.com/css2?family=Exo+2:wght@600;700&display=swap">
<style>
  :root {
    --page-bg: #1a1620;
    --card-ink: #0d0a1f;
    --deep-purple: #3a1260;
    --violet: #7b3fb0;
    --magenta: #a04cc0;
    --ice-blue: #5fb6e8;
    --text-light: #eef0ff;
    --text-lilac: #dcd2ff;
  }
  * { box-sizing: border-box; margin: 0; padding: 0; }
  html, body {
    width: 1200px;
    height: 1200px;
    overflow: hidden;
    background: var(--page-bg);
    font-family: "Exo 2", sans-serif;
  }
  .sheet {
    width: 1200px;
    height: 1200px;
    display: flex;
    flex-direction: column;
    align-items: center;
    justify-content: center;
    gap: 60px;
  }
  .card {
    position: relative;
    width: 910px;
    height: 520px;
    border-radius: 6px;
    overflow: hidden;
    color: var(--text-light);
    background:
      radial-gradient(ellipse 45% 55% at 38% 45%, rgba(95,182,232,0.75), transparent 70%),
      radial-gradient(ellipse 55% 60% at 72% 55%, rgba(160,76,192,0.8), transparent 72%),
      radial-gradient(ellipse 50% 60% at 12% 70%, rgba(123,63,176,0.7), transparent 70%),
      linear-gradient(135deg, var(--card-ink) 0%, var(--deep-purple) 50%, var(--card-ink) 100%);
  }
  .card--front {
    display: flex;
    flex-direction: column;
    align-items: center;
    justify-content: center;
  }
  .eye-artwork {
    width: 420px;
    height: 170px;
    border-radius: 50%;
    background: radial-gradient(ellipse at center, rgba(230,235,255,0.55), rgba(95,182,232,0.25) 45%, transparent 72%);
  }
  .dj-name {
    margin-top: 6px;
    font-size: 118px;
    font-weight: 700;
    line-height: 1;
    letter-spacing: 2px;
    color: var(--text-light);
  }
  .dj-role {
    margin-top: 22px;
    font-size: 30px;
    font-weight: 700;
    color: var(--text-lilac);
    letter-spacing: 0.5px;
  }
  .card--back {
    display: flex;
    flex-direction: column;
    justify-content: center;
    padding: 0 70px;
    gap: 22px;
  }
  .genres {
    font-size: 30px;
    font-weight: 700;
    color: var(--text-light);
  }
  .contact-list {
    list-style: none;
    display: flex;
    flex-direction: column;
    gap: 16px;
    margin-top: 14px;
  }
  .contact-item {
    display: flex;
    align-items: center;
    gap: 16px;
    font-size: 27px;
    font-weight: 600;
    color: var(--text-lilac);
  }
  .contact-item svg { flex: none; }
</style>
</head>
<body>
  <main class="sheet">
    <section class="card card--front" aria-label="Card front">
      <div class="eye-artwork" role="img" aria-label="Sketched eye illustration with fine light strokes"></div>
      <h1 class="dj-name">Voxtel</h1>
      <p class="dj-role">Professional DJ (West Coast)</p>
    </section>

    <section class="card card--back" aria-label="Card back">
      <p class="genres">EDM (Deep/House/Techno), Hip Hop, Latin, Trap.</p>
      <ul class="contact-list">
        <li class="contact-item">
          <svg width="26" height="26" viewBox="0 0 24 24" aria-hidden="true"><path fill="#dcd2ff" d="M6.6 10.8a15 15 0 0 0 6.6 6.6l2.2-2.2a1 1 0 0 1 1-.25 11.4 11.4 0 0 0 3.6.57 1 1 0 0 1 1 1V20a1 1 0 0 1-1 1A17 17 0 0 1 3 4a1 1 0 0 1 1-1h3.5a1 1 0 0 1 1 1c0 1.25.2 2.45.57 3.57a1 1 0 0 1-.25 1z"/></svg>
          <span>Cell: 555-274-9163</span>
        </li>
        <li class="contact-item">
          <svg width="26" height="26" viewBox="0 0 24 24" aria-hidden="true"><rect x="2.5" y="5" width="19" height="14" rx="2" fill="none" stroke="#dcd2ff" stroke-width="2"/><path d="M3 6l9 7 9-7" fill="none" stroke="#dcd2ff" stroke-width="2"/></svg>
          <span>Email: Voxtelofficial@mailnest.net</span>
        </li>
        <li class="contact-item">
          <svg width="26" height="26" viewBox="0 0 24 24" aria-hidden="true"><circle cx="12" cy="12" r="9.5" fill="none" stroke="#dcd2ff" stroke-width="2"/><path d="M2.5 12h19M12 2.5c3 3 3 16 0 19M12 2.5c-3 3-3 16 0 19" fill="none" stroke="#dcd2ff" stroke-width="1.6"/></svg>
          <span>www.beatcloudia.net/yourtuneisfading</span>
        </li>
      </ul>
    </section>
  </main>
</body>
</html>
```